Real Estate Sign Project

We need a Real Estate sign that promotes the property being listed and our company and agent listing the property. The images need to be able to be swapped out so we can use the template for each listing we have. I have a sample from another company that shows what were are trying to accomplish. Would want ours to be unique using our logo and the colors in our logo. We would like to not have to use a rider. Would want agents name and phone number to be part of the 36" x 24" sign.

Industry/Entity Type

Real Estate

Requirements
Must have
• Sign dimensions are 36 inches by 24 inches (36" across and 24" up down). Use example.of.sign.we.want.jpg as the direction we want to go but with a different layout and our logo and colors. This would be just a template that we can swap out new pictures, address, price, website, agents contact info for each home we are listing. Like the idea of the pictures bleeding off the sides. Please use free stock photos for the home images as we will be changing these out for each listing. Please incorporate all info including agents info into the one sign. File must be layered so we can change the pictures, price, website, agent, etc. We use GIMP (.xcf) file

```html
<!DOCTYPE html>
<html lang="en">
<head>
<meta charset="utf-8">
<title>Home For Sale – 4127 Willow Lane</title>
<link rel="stylesheet" href="https://fonts.googleapis.com/css2?family=Montserrat:wght@600;700&family=Questrial&display=swap">
<style>
  :root {
    --navy: #1b2a5c;
    --sky: #1d8fd2;
    --orange: #e9652b;
    --white: #ffffff;
    --grey-light: #f6f6f6;
    --grey-mid: #d6d7d9;
    --gap: #ffffff;
  }
  * { margin: 0; padding: 0; box-sizing: border-box; }
  html, body { width: 1200px; height: 800px; overflow: hidden; background: var(--white); }
  .sign {
    position: relative;
    width: 1200px;
    height: 800px;
    overflow: hidden;
    font-family: "Questrial", "Century Gothic", sans-serif;
    background: var(--gap);
  }
  .brand {
    position: absolute; left: 0; top: 0; width: 248px; height: 146px;
    background: var(--white);
    display: flex; align-items: center; justify-content: center; gap: 10px;
  }
  .brand-dot { width: 26px; height: 26px; border-radius: 50%; background: var(--orange); flex: none; }
  .brand-name {
    font-family: "Montserrat", sans-serif; font-weight: 700; font-size: 24px;
    line-height: 1.05; color: var(--navy); width: 150px;
  }
  .headline {
    position: absolute; left: 248px; top: 0; right: 0; height: 146px;
    background: var(--navy); color: var(--white);
    display: flex; align-items: center; justify-content: flex-end; padding-right: 24px;
  }
  .headline-label { font-size: 34px; margin-right: 28px; margin-top: 32px; }
  .headline-price {
    font-family: "Montserrat", sans-serif; font-weight: 700; font-size: 90px;
    letter-spacing: -1px; line-height: 1;
  }
  .photo { position: absolute; }
  .photo-bath { left: 0; top: 146px; width: 432px; height: 315px;
    background: linear-gradient(100deg, #d9d4cc 0%, #f1efec 45%, #c9c3bb 80%, #6e4a2e 100%); }
  .photo-bedroom { left: 438px; top: 146px; width: 484px; height: 315px;
    background: linear-gradient(180deg, #bfb7ad 0%, #8e7f70 40%, #7a6a58 70%, #5e4c3c 100%); }
  .photo-living { left: 930px; top: 146px; width: 270px; height: 174px;
    background: linear-gradient(160deg, #e6d6b8 0%, #b88b5b 55%, #7b4a26 100%); }
  .photo-kitchen { left: 930px; top: 326px; width: 270px; height: 177px;
    background: linear-gradient(170deg, #cfa97a 0%, #b98c5b 50%, #8b6a4d 100%); }
  .photo-exterior { left: 930px; top: 509px; width: 270px; height: 174px;
    background: linear-gradient(180deg, #3f7fd0 0%, #9cc3ea 40%, #c9ccd0 60%, #4f8a35 85%, #3d7328 100%); }
  .details {
    position: absolute; left: 0; top: 461px; width: 930px; height: 222px;
    background: linear-gradient(180deg, var(--grey-light) 0%, var(--grey-mid) 100%);
    color: var(--navy);
  }
  .address { position: absolute; left: 22px; top: 84px; font-size: 51px; white-space: nowrap; }
  .brace { position: absolute; left: 468px; top: 18px; }
  .features { position: absolute; left: 514px; top: 14px; list-style: none; font-size: 33px; line-height: 40px; }
  .web-bar {
    position: absolute; left: 0; top: 686px; width: 1200px; height: 45px;
    background: var(--sky); color: var(--white); font-size: 30px;
    display: flex; align-items: center; padding-left: 298px;
  }
  .agent-bar {
    position: absolute; left: 0; top: 731px; width: 1200px; height: 69px;
    background: var(--navy); color: var(--white);
    display: flex; align-items: center; padding: 0 28px;
    font-family: "Montserrat", sans-serif; font-weight: 700;
  }
  .agent-dot { width: 36px; height: 36px; border-radius: 50%; background: var(--orange); margin-right: 16px; }
  .agent-label { color: var(--sky); font-size: 31px; margin-right: 12px; }
  .agent-name { font-size: 31px; }
  .agent-phone { margin-left: auto; font-size: 34px; letter-spacing: 1px; margin-top: -14px; }
</style>
</head>
<body>
<main class="sign">
  <div class="brand">
    <span class="brand-dot"></span>
    <span class="brand-name">Larkfield Realty</span>
  </div>
  <header class="headline">
    <span class="headline-label">Home For Sale</span>
    <span class="headline-price">$360,000</span>
  </header>

  <div class="photo photo-bath" role="img" aria-label="Bathroom photo with glass shower enclosure"></div>
  <div class="photo photo-bedroom" role="img" aria-label="Master bedroom photo with bed and pendant lamps"></div>
  <div class="photo photo-living" role="img" aria-label="Living room photo with fireplace and wood floors"></div>
  <div class="photo photo-kitchen" role="img" aria-label="Kitchen photo with granite island and wood cabinets"></div>
  <div class="photo photo-exterior" role="img" aria-label="Exterior photo of the two-storey house and lawn"></div>

  <section class="details">
    <h1 class="address" style="font-weight:400">4127 Willow Lane</h1>
    <svg class="brace" width="40" height="186" viewBox="0 0 40 186" aria-hidden="true">
      <path d="M34 3 C18 3 18 10 18 24 L18 72 C18 86 14 92 4 93 C14 94 18 100 18 114 L18 162 C18 176 18 183 34 183"
            fill="none" stroke="var(--navy)" stroke-width="4" stroke-linecap="round"/>
    </svg>
    <ul class="features">
      <li>4 Bedrooms</li>
      <li>3.5 Baths</li>
      <li>3200 Finished SF</li>
      <li>2-Car Garage</li>
    </ul>
  </section>

  <div class="web-bar">LarkfieldRealty.com/4127Willow</div>

  <footer class="agent-bar">
    <span class="agent-dot"></span>
    <span class="agent-label">AGENT:</span>
    <span class="agent-name">Jane Marlow</span>
    <span class="agent-phone">xxx/xxx/xxxx</span>
  </footer>
</main>
</body>
</html>
```